Business Card Design

Harbor Refuse 342 is a waste collection business contracted to remove waste from city streets, parks and caravan parks.

Target Market(s)

CEO and Managing Directors

Industry/Entity Type

Business

Contact Information for Business Card

Harbor Refuse 342
Manager
Dale Pickett
0439516204
harborrefuse342@quillmail.com.au

Colors
33a6d7
ecf7fb

Requirements
Must have
• Must have eye catching design that stands out above others ( tender process can be very competitive ).
Nice to have
• A garbage truck on or in the logo somehow

```html
<!DOCTYPE html>
<html lang="en">
<head>
<meta charset="utf-8">
<title>Harbor Refuse 342 – Business Card</title>
<link rel="stylesheet" href="https://fonts.googleapis.com/css2?family=Open+Sans:wght@400;600&display=swap">
<style>
  :root {
    --brand-blue: #33a6d7;
    --brand-tint: #ecf7fb;
    --ink: #1a1a1a;
    --paper: #ffffff;
    --backdrop: #d9d9d9;
  }
  * { margin: 0; padding: 0; box-sizing: border-box; }
  html, body {
    width: 1200px;
    height: 900px;
    overflow: hidden;
    background: var(--backdrop);
    font-family: "Open Sans", Arial, sans-serif;
  }
  .business-card {
    position: absolute;
    left: 180px;
    top: 210px;
    width: 840px;
    height: 480px;
    background: var(--paper);
    overflow: hidden;
    box-shadow: 0 6px 18px rgba(0,0,0,0.18);
  }
  .rule {
    position: absolute;
    left: 0;
    width: 100%;
    height: 3px;
    background: var(--brand-blue);
  }
  .rule--top { top: 24px; }
  .rule--under-band { top: 136px; }
  .rule--above-footer { top: 414px; }
  .title-band {
    position: absolute;
    left: 0;
    top: 34px;
    width: 100%;
    height: 96px;
    background: var(--brand-blue);
    display: flex;
    align-items: center;
    padding-left: 48px;
  }
  .company-name {
    color: var(--paper);
    font-weight: 400;
    font-size: 60px;
    letter-spacing: 1px;
    text-transform: uppercase;
    line-height: 1;
    white-space: nowrap;
  }
  .truck-illustration {
    position: absolute;
    left: 490px;
    top: 150px;
    width: 350px;
    height: 250px;
    border-radius: 6px 0 0 6px;
    background: linear-gradient(135deg, #bfe3f3, var(--brand-tint));
  }
  .contact {
    position: absolute;
    left: 64px;
    top: 222px;
    width: 410px;
  }
  .contact__name {
    color: var(--brand-blue);
    font-size: 32px;
    font-weight: 400;
    text-transform: uppercase;
    line-height: 1.15;
  }
  .contact__role {
    color: var(--ink);
    font-size: 24px;
    font-weight: 600;
    line-height: 1.2;
  }
  .contact__line {
    display: flex;
    align-items: center;
    gap: 12px;
    color: var(--ink);
    white-space: nowrap;
  }
  .contact__phone {
    margin-top: 22px;
    font-size: 28px;
    font-weight: 600;
    letter-spacing: 1px;
  }
  .contact__email {
    margin-top: 10px;
    font-size: 19px;
    font-weight: 400;
  }
  .contact-icon { width: 26px; height: 26px; flex: none; }
  .footer-band {
    position: absolute;
    left: 0;
    top: 426px;
    width: 100%;
    height: 54px;
    background: var(--brand-blue);
  }
</style>
</head>
<body>
  <div class="business-card">
    <div class="rule rule--top"></div>
    <div class="title-band">
      <h1 class="company-name">Harbor Refuse 342</h1>
    </div>
    <div class="rule rule--under-band"></div>

    <div class="truck-illustration" role="img" aria-label="Line sketch of a skip bin truck"></div>

    <div class="contact">
      <p class="contact__name">Dale Pickett</p>
      <p class="contact__role">Manager</p>
      <p class="contact__line contact__phone">
        <svg class="contact-icon" viewBox="0 0 24 24" aria-hidden="true">
          <circle cx="12" cy="12" r="10.5" fill="none" stroke="#1a1a1a" stroke-width="1.6"/>
          <path d="M8.6 7.2c.4-.4 1-.4 1.3 0l1.1 1.4c.3.4.2.9-.1 1.2l-.6.6c.5 1.1 1.4 2 2.5 2.5l.6-.6c.3-.3.8-.4 1.2-.1l1.4 1.1c.4.3.4.9 0 1.3l-.8.8c-.5.5-1.3.6-1.9.3-2.3-1-4.2-2.9-5.2-5.2-.3-.6-.2-1.4.3-1.9z" fill="#1a1a1a"/>
        </svg>
        0439516204
      </p>
      <p class="contact__line contact__email">
        <svg class="contact-icon" viewBox="0 0 24 24" aria-hidden="true">
          <circle cx="12" cy="12" r="10.5" fill="none" stroke="#1a1a1a" stroke-width="1.6"/>
          <rect x="6.5" y="8.5" width="11" height="7.5" fill="none" stroke="#1a1a1a" stroke-width="1.4"/>
          <path d="M6.5 8.5l5.5 4.2 5.5-4.2" fill="none" stroke="#1a1a1a" stroke-width="1.4"/>
        </svg>
        harborrefuse342@quillmail.com.au
      </p>
    </div>

    <div class="rule rule--above-footer"></div>
    <div class="footer-band"></div>
  </div>
</body>
</html>
```